Bluestone Nine LLC Flyer Design

Marketing Materials for Real Estate Company. This flyer will be used to promote the company throughout the Commercial Real Estate business in the United States. The team has been together for 15 years. We are the middle guys between the Tenant, Broker, and the Owner. In the case of working with a Franchisor, we will be their Plug and Play leasing arm that will assist their new Franchisee's with their site selection, lease negotiations, design and construction management.

Target Market(s)

Real Estate Owners, Franchisor's, and Brokers

Font styles to use
Serif

Colors

Designer to choose colors to be used in the design.

Requirements
Must have
• The flyer must have......
• 1. The Best Leasing Machine On The Planet
• 2. Over the past 15 years our group has completed 4,492 lease transactions resulting in leasing 17,803,114 square feet in shopping centers across the United States.
• 3. Plug and Play Leasing Specialists. We handle the details between when the broker shows up with the space and the tenant and completing the lease negotiations, legal negotiations and documentation, and construction management to Certificate of Occupancy.
• 4. For Information Call Colette Varga at 555-014-2763 or Wendy Falk at 555-017-8302.
Nice to have
• National Tenants the we have completed transactions with....
• Pellmart, Fresh Basket, Harbor Pams, Vexo, Dunn, QV Rendo, Burrasco, Pattersons, Wrap Shack, Brewhorns, Summit Workout, ShipVo, Tredwell, PKN, Halvorsons, Q&L, Ledger Union Bank, Hen Haus-O, Lotus Kitchen, Furvo, Dex-Mart, Fieldly, and Orbit Theaters

```html
<!DOCTYPE html>
<html lang="en">
<head>
<meta charset="utf-8">
<title>Bluestone Nine LLC Flyer</title>
<link rel="stylesheet" href="https://fonts.googleapis.com/css2?family=Bebas+Neue&family=Lato:wght@400;700&family=Comfortaa:wght@600&display=swap">
<style>
  :root {
    --backdrop: #333333;
    --paper: #ffffff;
    --ink: #111111;
    --green: #a4c95a;
    --green-dark: #8fb845;
    --icon-ink: #2e3a22;
  }
  html, body { margin: 0; padding: 0; width: 1200px; height: 1200px; overflow: hidden; background: var(--backdrop); }
  .flyer {
    position: absolute; left: 278px; top: 170px;
    width: 790px; height: 1107px;
    transform: scale(0.8); transform-origin: top left;
    background: var(--paper); overflow: hidden;
    box-shadow: 0 10px 30px rgba(0,0,0,.5);
    font-family: 'Lato', sans-serif; color: var(--ink);
  }
  .shapes { position: absolute; inset: 0; }
  .brand {
    position: absolute; left: 496px; top: 30px; width: 258px;
    font-family: 'Comfortaa', sans-serif; font-weight: 600; font-size: 23px;
    color: var(--green); letter-spacing: 1px; border-top: 3px solid var(--green); padding-top: 4px;
  }
  .headline { position: absolute; left: 496px; top: 100px; margin: 0; font-family: 'Bebas Neue', sans-serif; font-weight: 400; line-height: .95; }
  .headline span { display: block; }
  .headline .l1 { font-size: 62px; }
  .headline .l2 { font-size: 50px; }
  .headline .l3 { font-size: 62px; color: var(--green); }
  .headline-rule { position: absolute; left: 625px; top: 264px; width: 165px; height: 6px; background: var(--ink); }
  .stats { position: absolute; left: 501px; top: 284px; width: 270px; margin: 0; font-size: 15px; line-height: 18.5px; }
  .specialists { position: absolute; left: 29px; top: 684px; margin: 0; font-family: 'Bebas Neue', sans-serif; font-weight: 400; line-height: .98; }
  .specialists span { display: block; font-size: 48px; }
  .specialists .accent { color: var(--green); }
  .services { position: absolute; left: 32px; top: 782px; width: 440px; margin: 0; font-size: 12.4px; line-height: 15.5px; letter-spacing: -.1px; }
  .section-title { position: absolute; left: 30px; margin: 0; font-family: 'Bebas Neue', sans-serif; font-weight: 400; font-size: 23px; display: flex; align-items: center; gap: 10px; }
  .section-title::after { content: ""; height: 3px; background: var(--green); }
  .info-title { top: 840px; }
  .info-title::after { width: 158px; }
  .tenants-title { top: 990px; }
  .tenants-title::after { width: 98px; }
  .contact { position: absolute; top: 868px; width: 160px; text-align: center; font-size: 15px; line-height: 18px; }
  .contact .avatar { width: 72px; height: 72px; margin: 0 auto 10px; display: block; }
  .contact .phone { color: var(--green); }
  .contact-a { left: 23px; }
  .contact-b { left: 280px; }
  .contact-divider { position: absolute; left: 231px; top: 880px; width: 2px; height: 88px; background: var(--ink); }
  .tenant-list { position: absolute; left: 30px; top: 1022px; width: 590px; margin: 0; padding: 0; list-style: none; display: flex; flex-wrap: wrap; gap: 5px 9px; }
  .tenant-list li { font-size: 9px; line-height: 11px; font-weight: 700; color: var(--ink); display: flex; align-items: center; gap: 3px; }
  .tenant-list li::before { content: ""; width: 8px; height: 8px; border-radius: 50%; background: var(--green-dark); }
  .base-bar { position: absolute; left: 0; top: 1088px; width: 625px; height: 19px; background: var(--ink); }
</style>
</head>
<body>
<main class="flyer">
  <svg class="shapes" width="790" height="1107" viewBox="0 0 790 1107">
    <defs>
      <linearGradient id="suit" x1="0" y1="0" x2="1" y2="1">
        <stop offset="0" stop-color="#2a4563"/><stop offset="1" stop-color="#0e1d30"/>
      </linearGradient>
      <linearGradient id="towers" x1="0" y1="0" x2="0" y2="1">
        <stop offset="0" stop-color="#8fc3ea"/><stop offset=".5" stop-color="#2f73c4"/><stop offset="1" stop-color="#1c4f94"/>
      </linearGradient>
      <linearGradient id="home" x1="0" y1="0" x2="0" y2="1">
        <stop offset="0" stop-color="#b8d6ef"/><stop offset=".55" stop-color="#b9a78c"/><stop offset="1" stop-color="#4e8a3a"/>
      </linearGradient>
    </defs>
    <polygon points="0,509 195,628 113,672 0,607" fill="var(--green)"/>
    <polygon role="img" aria-label="Photo of a hand in a dark suit holding a model house" points="0,0 484,0 484,472 195,628 0,509" fill="url(#suit)"/>
    <polygon role="img" aria-label="Photo of a suburban home with a garden" points="365,560 443,605 443,695 365,740 287,695 287,605" fill="url(#home)"/>
    <polygon role="img" aria-label="Photo of glass office towers against a blue sky" points="616,419 773,510 773,703 616,794 458,703 458,510" fill="url(#towers)"/>
    <polygon points="645,827 790,737 790,1107 645,1107" fill="var(--green)"/>
  </svg>

  <div class="brand">Bluestone Nine LLC</div>

  <h1 class="headline"><span class="l1">The Best</span><span class="l2">Leasing Machine</span><span class="l3">On The Planet</span></h1>
  <div class="headline-rule"></div>

  <p class="stats">Over the past <b>15</b> years our group has completed <b>4,492</b> lease transactions resulting in leasing <b>17,803,114</b> square feet in shopping centers across the United States.</p>

  <h2 class="specialists"><span>Plug &amp; Play</span><span class="accent">Leasing Specialists</span></h2>
  <p class="services">We handle the details between when the broker shows up with the space and the tenant and completing the lease negotiations, legal negotiations and documentation, and construction management to Certificate of Occupancy.</p>

  <h3 class="section-title info-title">For Information Call</h3>

  <div class="contact contact-a">
    <svg class="avatar" viewBox="0 0 72 72" aria-hidden="true"><circle cx="36" cy="36" r="36" fill="var(--green)"/><circle cx="36" cy="26" r="9" fill="var(--icon-ink)"/><path d="M20 52 q0-14 16-14 q16 0 16 14 z" fill="var(--icon-ink)"/><rect x="16" y="52" width="40" height="3" fill="var(--icon-ink)"/></svg>
    <div>Colette Varga</div>
    <div>at <span class="phone">555-014-2763</span></div>
  </div>
  <div class="contact-divider"></div>
  <div class="contact contact-b">
    <svg class="avatar" viewBox="0 0 72 72" aria-hidden="true"><circle cx="36" cy="36" r="36" fill="var(--green)"/><circle cx="36" cy="26" r="9" fill="var(--icon-ink)"/><path d="M20 52 q0-14 16-14 q16 0 16 14 z" fill="var(--icon-ink)"/><rect x="16" y="52" width="40" height="3" fill="var(--icon-ink)"/></svg>
    <div>Wendy Falk</div>
    <div>at <span class="phone">555-017-8302.</span></div>
  </div>

  <h3 class="section-title tenants-title">National Tenants the we have completed transactions with</h3>
  <ul class="tenant-list">
    <li>Vexo</li><li>Fresh Basket</li><li>QV Rendo</li><li>Hen Haus-O</li><li>Dunn</li><li>Brewhorns</li><li>Q&amp;L</li><li>Ledger Union Bank</li><li>Burrasco</li><li>Pellmart</li><li>ShipVo</li><li>Pattersons</li>
    <li>Lotus Kitchen</li><li>Furvo</li><li>Summit Workout</li><li>Fieldly</li><li>Wrap Shack</li><li>Harbor Pams</li><li>Halvorsons</li><li>Dex-Mart</li><li>PKN</li><li>Orbit Theaters</li><li>Tredwell</li>
  </ul>

  <div class="base-bar"></div>
</main>
</body>
</html>
```